Redesign of page from emergency manual

Please redesign this PDF to look better. Please don't include any stock photos. It must be legible. Making some words bold is probably a good idea.

Here are some things I like :

https://tarrowbooks.com.au/collections/frontpage/products/the-plk-v2-ebook

https://img-cd.vostramediafiles.com/qa-ejkwPLOTYY_SuCKbZNu411Qwgjv8YssPxEdzXN93hDkSRjLXK8WmfgbmrJW4ZZ3yUPK=w1052-h592-rw

```html
<!DOCTYPE html>
<html lang="en">
<head>
<meta charset="utf-8">
<title>Hypertension, Acute</title>
<link rel="stylesheet" href="https://fonts.googleapis.com/css2?family=Bebas+Neue&family=Arimo:wght@400;700&display=swap">
<style>
:root{
  --navy:#0b4a8b;
  --navy-dark:#0a5a8a;
  --teal:#3cb2c6;
  --ice:#d3ecf9;
  --sky:#b6def5;
  --row:#cfe9f8;
  --ink:#1a1a1a;
  --white:#ffffff;
}
*{box-sizing:border-box;margin:0;padding:0}
html,body{width:1200px;height:1000px;overflow:hidden;background:var(--white);font-family:"Arimo",Arial,sans-serif;color:var(--ink)}
.card{position:absolute;left:315px;top:115px;width:570px;height:767px;background:var(--navy);overflow:hidden}
.card-title{position:absolute;left:0;top:26px;width:100%;height:70px;overflow:hidden;text-align:center;white-space:nowrap;font-family:"Bebas Neue",Impact,sans-serif;font-weight:400;font-size:70px;line-height:70px;color:var(--ice);letter-spacing:1.5px}
.subtitle{position:absolute;left:8px;right:8px;top:107px;height:54px;background:var(--teal);color:var(--white);text-align:center;font-weight:700;font-size:17px;letter-spacing:1.6px;line-height:21px;padding-top:6px}
.intro{position:absolute;left:8px;right:8px;top:161px;height:242px;background:var(--white)}
.notes{position:absolute;left:9px;top:10px;width:290px;font-size:12.6px;line-height:19px;text-align:justify}
.notes .lead{padding-left:14px;position:relative}
.notes .lead::before{content:"";position:absolute;left:0;top:5px;width:9px;height:9px;border-radius:50%;background:var(--navy)}
.notes ul{list-style:none;padding-left:14px}
.notes li{padding-left:12px;position:relative}
.notes li::before{content:"•";position:absolute;left:0}
.notes li.sub{font-size:11.6px}
.notes li.sub::before{content:"-"}
.bp-table{position:absolute;left:324px;top:11px;width:220px;border-collapse:separate;border-spacing:0;font-size:12px;text-align:center}
.bp-table caption{background:var(--navy-dark);color:var(--white);font-weight:700;font-size:12px;padding:8px 0;white-space:nowrap}
.bp-table th{background:var(--teal);color:var(--white);font-weight:700;height:30px;border-right:3px solid var(--white);border-top:3px solid var(--white)}
.bp-table td{background:var(--row);height:28px;border-right:3px solid var(--white);border-top:3px solid var(--white)}
.bp-table th:last-child,.bp-table td:last-child{border-right:0}
.bp-table tr:last-child td:first-child{border-bottom-left-radius:14px}
.bp-table tr:last-child td:last-child{border-bottom-right-radius:14px}
.caution{position:absolute;left:9px;right:10px;top:178px;font-size:12.6px;line-height:18px;text-align:justify}
.lower{position:absolute;left:8px;right:8px;top:403px;height:357px;background:var(--sky)}
.drug-table{position:absolute;left:11px;top:0;width:533px;height:255px;background:var(--white);border:2px solid var(--navy-dark);border-top:0;border-bottom-right-radius:16px;overflow:hidden}
.drug-head{display:flex;height:27px;background:var(--navy-dark);color:var(--white);font-weight:700;font-size:15px;line-height:27px}
.drug-head .col-action{width:150px;text-align:center}
.drug-head .col-drug{flex:1;text-align:center}
.drug-row{display:flex;border-top:2px solid var(--navy-dark);font-size:12px;line-height:18px}
.drug-row .col-action{width:150px;border-right:2px solid var(--navy-dark);padding:13px 0 0 18px}
.drug-row .col-drug{flex:1;padding:10px 14px 0 10px}
.drug-row ul{list-style:none}
.drug-row li{padding-left:14px;position:relative}
.drug-row li::before{content:"";position:absolute;left:0;top:6px;width:6px;height:6px;background:var(--navy)}
.row-a{height:62px}
.row-b{height:126px}
.row-c{height:38px}
.row-c .col-action{padding-top:10px}
.gap{height:18px}
.diff-title{position:absolute;left:0;right:0;top:266px;text-align:center;font-weight:700;font-size:13px}
.diff{position:absolute;left:10px;top:290px;display:flex;font-size:11px;line-height:12.5px}
.diff ul{list-style:none;padding:0 12px}
.diff li{padding-left:11px;position:relative}
.diff li::before{content:"•";position:absolute;left:0}
.diff ul+ul{border-left:2px solid var(--navy)}
.diff .c1{width:166px;padding-left:0}
.diff .c2{width:206px;padding-right:30px}
.diff .c3{width:150px}
</style>
</head>
<body>
<article class="card">
  <h1 class="card-title">HYPERTENSION, ACUTE</h1>
  <p class="subtitle">SUSTAINED HIGH BLOOD PRESSURE REFRACTORY<br>TO TREATING REVERSIBLE CAUSES</p>

  <section class="intro">
    <div class="notes">
      <p class="lead">In pediatrics, hypertension is almost always treated by addressing likely causes such as light anesthesia or measurement error:</p>
      <ul>
        <li>Ensure correct BP cuff size: cuff bladder width ~40% of limb circumference</li>
        <li>Ensure arterial line transducer is at level of heart</li>
        <li class="sub">Consider placing arterial line if not already present</li>
      </ul>
    </div>
    <table class="bp-table">
      <caption>Hypertensive Blood Pressure Range*</caption>
      <tr><th>Age (yr)</th><th>Systolic</th><th>Diastolic</th></tr>
      <tr><td>newborn</td><td>&gt;97</td><td>&gt;70</td></tr>
      <tr><td>1-3</td><td>&gt;105</td><td>&gt;61</td></tr>
      <tr><td>4-12</td><td>&gt;113</td><td>&gt;86</td></tr>
    </table>
    <p class="caution"><b>CAUTION:</b> Anti-hypertensive drugs are almost never needed for routine pediatric cases. These medications are used almost exclusively for specialized cardiac, neurosurgical, or endocrine (pheochromocytoma) cases. Consult an expert before use. Rule-out increased ICP.</p>
  </section>

  <section class="lower">
    <div class="drug-table">
      <div class="drug-head"><div class="col-action">Action</div><div class="col-drug">Drug (IV Dosing)</div></div>
      <div class="drug-row row-a">
        <div class="col-action">Direct smooth<br>Muscle Relaxation</div>
        <div class="col-drug"><ul>
          <li>Sodium nitroprusside 0.5-10 MICROgrams/kg/min</li>
          <li>HydrALAZINE 0.1-0.2 mg/kg (adult dose 5-10 mg)</li>
        </ul></div>
      </div>
      <div class="drug-row row-b">
        <div class="col-action">ß-Adrenergic<div class="gap"></div><div class="gap"></div><div class="gap"></div>Calcium channel<br>Blockade</div>
        <div class="col-drug"><ul>
          <li>Esmolol 100-500 MICROgrams/kg over 5 min, then Blockade 25-300 MICROgrams/kg/min</li>
          <li>Labetalol (also a effect) 0.2-1 mg/kg q 10 min; 0.4-3 mg/kg/hour (Infusion)</li>
          <li>niCARdapine 0.5-5 MICROgrams/kg/min</li>
          <li>Clevidipine 0.5-3.5 MICROgrams/kg/min</li>
        </ul></div>
      </div>
      <div class="drug-row row-c">
        <div class="col-action">D1-dopamine agonist</div>
        <div class="col-drug"><ul><li>Fenoldopam 0.2-0.8 MICROgrams/kg/min</li></ul></div>
      </div>
    </div>

    <h2 class="diff-title">Consider Differential (Partial):</h2>
    <div class="diff">
      <ul class="c1">
        <li>Light anesthesia (consider vaporizer or infusion pump empty or malfunctioning)</li>
        <li>Hypercarbia</li>
      </ul>
      <ul class="c2">
        <li>Hypoxemia</li>
        <li>Arterial line transducer too low or BP cuff too small</li>
        <li>Withdrawal (EtOH or opioid)</li>
      </ul>
      <ul class="c3">
        <li>Thyroid Storm</li>
        <li>Pheochromocytoma</li>
        <li>Drug Error</li>
      </ul>
    </div>
  </section>
</article>
</body>
</html>
```